Tor Ridge Wine Club-The Onyx Roll

We are a new aspirational brand of fine Tasmania Wine. We need a commitment club poster which appeals to the ego.We have one opportunity to get customers to sign up and that is when they visit at the cellar door. This club is the core of our business.

The brand is a clean, pure , simple brand, black and white very sophiscated.
This is a top end product.

Our Commitment Club is named The Onyx Roll which is a play on words. Tradionally The Onyx Roll is a list of people that you dont want to do business with. So we are turning this on its had.

You need to make this poster sharp, desirable, possibly sexy but masculine. Im thinking Felix Crane . It doesnt matter the client will be 40 up fashion consious looking for something new , exclusive , something there peers don't have.

I dont like busy! make it clean clear and basically undeniable. The client must not be able to resist the offer.

www.torridgevines.com.au

Reason: Internet problems so cant get to respond and offer comment in a timely manner

Appreciator 40-60 male wants to be recognised fashion consious sophiscated has money and wants to part of something exclusive.

A feeling that you are part of something that only a few are. Exclusive

Maybe an imagine of beautiful people 30/40ish I want to be drinking Tor Wine / in The Onyx Roll

Fashion

Must have
• Tor Ridge Logo
TOR Bottles images

We produce only 1600 cases of wine each vintage. Therefore we have limited membership 001-999 for our club.
Award Winning Wines available exclusively from us.

Gold Member
We will reserve 2 cases of our limited vintage, to be delivered to you in May and Oct.
Single varietal or mixed cases. You receive a 15% discount.

Silver Member
We will reserve 1 case of our limited vintage to be delivered to you 6 bottles in May and 6 in Oct.
Single varietal or mixed cases. You receive a 10% discount.

To you exclusively from us not, available from any other retailers.

You will be invited to Onyx Roll Only Events and Tastings.
You will get preferential access to new and limited releases.
Members will be entered in a bi annual draw to win a 2 night stay here at the Tor Weavers Cottage on the Freycinet Coast Tasmania.

• VIP stamps,gimacs, anything that cheapens our brand.

We do not like busy posters please have white space

```html
<!DOCTYPE html>
<html lang="en">
<head>
<meta charset="utf-8">
<title>Tor Ridge – Join the Onyx Roll</title>
<link rel="stylesheet" href="https://fonts.googleapis.com/css2?family=Cinzel:wght@400;500&family=Crimson+Text:wght@400;600&display=swap">
<style>
  :root {
    --page: #ffffff;
    --onyx: #1b1b1b;
    --onyx-deep: #0f0f0f;
    --gold: #b8962e;
    --gold-light: #e6c86a;
    --gold-dark: #8a6b1c;
    --silver-panel-light: #f6f6f6;
    --silver-panel-mid: #e3e3e3;
    --ink-dark: #2a2a2a;
    --ink-mid: #5c5c5c;
    --ink-soft: #8c8c8c;
    --ink-light: #f2f2f2;
    --ink-light-soft: #c9c9c9;
  }
  * { box-sizing: border-box; margin: 0; padding: 0; }
  html, body {
    width: 1200px; height: 837px; overflow: hidden;
    background: var(--page);
  }
  .canvas { position: relative; width: 1200px; height: 837px; }

  .poster {
    position: absolute; top: 9px; width: 573px; height: 819px;
    background: var(--onyx); overflow: hidden;
  }
  .poster--light { left: 17px; }
  .poster--dark { left: 609px; }

  .poster__texture {
    position: absolute; inset: 0;
    background: linear-gradient(135deg, #242424 0%, var(--onyx) 50%, var(--onyx-deep) 100%);
  }

  .panel {
    position: absolute; left: 72px; top: 95px; width: 432px; height: 588px;
    border: 7px solid var(--gold);
    border-image: linear-gradient(160deg, var(--gold-light), var(--gold) 40%, var(--gold-dark) 70%, var(--gold-light)) 1;
    text-align: center;
  }
  .poster--light .panel {
    background: linear-gradient(160deg, var(--silver-panel-light), var(--silver-panel-mid) 55%, var(--silver-panel-light));
  }
  .poster--dark .panel {
    background: linear-gradient(160deg, #2c2c2c, #1a1a1a 60%, #121212);
  }

  .line {
    position: absolute; left: 0; right: 0;
    transform: translateY(-50%); line-height: 1.2;
    font-family: "Crimson Text", Georgia, serif;
    white-space: nowrap;
  }

  .headline__kicker {
    font-family: "Cinzel", "Times New Roman", serif;
    font-size: 23px; letter-spacing: 1px; top: 62px;
  }
  .headline__title {
    font-family: "Cinzel", "Times New Roman", serif;
    font-size: 60px; font-weight: 500; letter-spacing: 1px; top: 106px;
  }
  .divider {
    position: absolute; left: 50%; top: 147px; width: 104px; height: 10px;
    transform: translateX(-50%);
  }

  .tiers__intro { font-size: 15px; top: 194px; }
  .tiers__gold { font-size: 21px; top: 221px; color: var(--gold); }
  .tiers__silver { font-size: 21px; top: 246px; }

  .benefit { font-size: 15px; }
  .exclusive { font-size: 15px; font-weight: 600; }

  .brand {
    font-family: "Crimson Text", Georgia, serif;
    font-size: 42px; top: 500px; letter-spacing: 1px;
  }

  .poster__url {
    position: absolute; left: 0; right: 0; top: 777px;
    transform: translateY(-50%);
    text-align: center; color: var(--ink-light);
    font-family: "Crimson Text", Georgia, serif;
    font-size: 15px; letter-spacing: 1.2px;
  }
  .poster__band {
    position: absolute; left: 0; right: 0; bottom: 0; height: 30px;
    background: linear-gradient(90deg, var(--gold-dark), var(--gold-light) 30%, var(--gold) 60%, var(--gold-light) 85%, var(--gold-dark));
  }

  /* light variant colours */
  .poster--light .headline__kicker { color: var(--ink-mid); }
  .poster--light .headline__title { color: var(--ink-dark); }
  .poster--light .tiers__intro,
  .poster--light .benefit { color: var(--ink-mid); }
  .poster--light .tiers__silver { color: var(--ink-soft); }
  .poster--light .exclusive,
  .poster--light .brand { color: var(--onyx); }
  .poster--light .divider line { stroke: var(--ink-dark); }
  .poster--light .divider rect { fill: var(--ink-dark); }

  /* dark variant colours */
  .poster--dark .headline__kicker,
  .poster--dark .headline__title,
  .poster--dark .tiers__intro,
  .poster--dark .tiers__silver,
  .poster--dark .exclusive,
  .poster--dark .brand { color: var(--ink-light); }
  .poster--dark .benefit { color: var(--ink-light-soft); }
  .poster--dark .divider line { stroke: var(--ink-light); }
  .poster--dark .divider rect { fill: var(--ink-light); }
</style>
</head>
<body>
<main class="canvas">

  <section class="poster poster--light">
    <div class="poster__texture" role="img" aria-label="Dark diagonal pinstripe texture"></div>
    <div class="panel">
      <p class="line headline__kicker">JOIN THE</p>
      <h1 class="line headline__title">ONYX ROLL</h1>
      <svg class="divider" viewBox="0 0 104 10">
        <line x1="0" y1="5" x2="40" y2="5" stroke-width="1"/>
        <line x1="64" y1="5" x2="104" y2="5" stroke-width="1"/>
        <rect x="42" y="1" width="20" height="8" role="img" aria-label="Small ornamental flourish"/>
      </svg>
      <p class="line tiers__intro">Two levels of commitment</p>
      <p class="line tiers__gold">Gold Membership</p>
      <p class="line tiers__silver">Silver Membership</p>
      <p class="line benefit" style="top:289px">Preferential access to first releases and limited releases</p>
      <p class="line benefit" style="top:313px">VIP access to Onyx Roll only tastings and events.</p>
      <p class="line benefit" style="top:337px">Sophisticated, exclusive, inviting</p>
      <p class="line exclusive" style="top:372px">Not available with other retailers</p>
      <p class="line exclusive" style="top:391px">Exclusively to you from us.</p>
      <p class="line brand">Tor Ridge</p>
    </div>
    <p class="poster__url">WWW.TORRIDGEVINES.COM.AU</p>
    <div class="poster__band"></div>
  </section>

  <section class="poster poster--dark">
    <div class="poster__texture" role="img" aria-label="Dark diagonal pinstripe texture"></div>
    <div class="panel">
      <p class="line headline__kicker">JOIN THE</p>
      <h1 class="line headline__title">ONYX ROLL</h1>
      <svg class="divider" viewBox="0 0 104 10">
        <line x1="0" y1="5" x2="40" y2="5" stroke-width="1"/>
        <line x1="64" y1="5" x2="104" y2="5" stroke-width="1"/>
        <rect x="42" y="1" width="20" height="8" role="img" aria-label="Small ornamental flourish"/>
      </svg>
      <p class="line tiers__intro">Two levels of commitment</p>
      <p class="line tiers__gold">Gold Membership</p>
      <p class="line tiers__silver">Silver Membership</p>
      <p class="line benefit" style="top:298px">Preferential access to first releases and limited releases</p>
      <p class="line benefit" style="top:321px">VIP access to Onyx Roll only tastings and events.</p>
      <p class="line benefit" style="top:346px">Sophisticated, exclusive, inviting</p>
      <p class="line exclusive" style="top:381px">Not available with other retailers</p>
      <p class="line exclusive" style="top:401px">Exclusively to you from us.</p>
      <p class="line brand">Tor Ridge</p>
    </div>
    <p class="poster__url">WWW.TORRIDGEVINES.COM.AU</p>
    <div class="poster__band"></div>
  </section>

</main>
</body>
</html>
```